Business cards and logo for Delcourt Law, P.A.

I need a business card and logo design for a new law firm in Miami, Florida called Delcourt Law, P.A. I, Theodore K. Delcourt, am the only lawyer in the firm. The law firm will mainly serve businesses but will also handle many other cases. Preferred colors are green and/or gray, but open minded to other suggestions.

Industry/Entity Type

Legal

Contact Information for Business Card

Phone Number TBD. Address is:
41 NE 3RD AVE STE 200
MIAMI, FL 33142

```html
<!DOCTYPE html>
<html lang="en">
<head>
<meta charset="utf-8">
<title>Delcourt Law, P.A. — Business Cards</title>
<link rel="stylesheet" href="https://fonts.googleapis.com/css2?family=Tinos:wght@400;700&display=swap">
<style>
  :root {
    --crimson: #a3264d;
    --crimson-light: #b8315a;
    --crimson-dark: #7e1737;
    --paper: #fbfbfb;
    --wave-grey: #cfcfcf;
    --ink-on-crimson: #ffffff;
    --backdrop: #ece9e4;
  }
  * { margin: 0; padding: 0; box-sizing: border-box; }
  html, body { width: 1200px; height: 780px; overflow: hidden; }
  body {
    background: var(--backdrop);
    font-family: "Tinos", "Times New Roman", serif;
    display: flex;
    align-items: center;
    justify-content: center;
    gap: 40px;
  }
  .card {
    position: relative;
    width: 540px;
    height: 309px;
    overflow: hidden;
    box-shadow: 0 6px 18px rgba(0,0,0,0.18);
  }

  /* Contact side */
  .card-contact { background: var(--paper); }
  .card-contact .wave { position: absolute; inset: 0; }
  .contact-block {
    position: absolute;
    left: 272px;
    top: 22px;
    color: var(--ink-on-crimson);
    line-height: 1.2;
  }
  .holder-name { font-size: 18px; letter-spacing: 0.5px; }
  .holder-title { font-size: 12px; opacity: 0.85; margin-top: 1px; }
  .address { margin-top: 14px; font-size: 12.5px; line-height: 1.3; }
  .contact-line {
    display: flex;
    align-items: center;
    gap: 7px;
    font-size: 12.5px;
    margin-top: 4px;
  }
  .address + .contact-line { margin-top: 8px; }
  .icon {
    width: 13px; height: 13px;
    background: rgba(255,255,255,0.9);
    display: inline-flex; align-items: center; justify-content: center;
    flex: none;
  }
  .firm-lockup {
    position: absolute;
    left: 60px;
    top: 228px;
    display: flex;
    align-items: center;
    gap: 14px;
    color: var(--crimson);
  }
  .firm-mark {
    width: 40px; height: 40px;
    background: var(--crimson);
    flex: none;
  }
  .firm-name { font-size: 20px; letter-spacing: 0.8px; text-transform: uppercase; white-space: nowrap; }
  .firm-person { font-size: 15px; margin-top: 2px; white-space: nowrap; }

  /* Firm side */
  .card-firm {
    background: radial-gradient(ellipse at 55% 40%, var(--crimson-light) 0%, var(--crimson) 45%, var(--crimson-dark) 100%);
    display: flex;
    align-items: center;
    justify-content: center;
  }
  .card-firm .firm-lockup {
    position: static;
    flex-direction: column;
    gap: 16px;
    color: var(--ink-on-crimson);
    text-align: center;
  }
  .card-firm .firm-mark { background: var(--ink-on-crimson); width: 46px; height: 46px; }
  .card-firm .firm-name { font-size: 22px; }
  .card-firm .firm-person { font-size: 16px; margin-top: 4px; }
</style>
</head>
<body>

  <section class="card card-contact" aria-label="Business card, contact side">
    <svg class="wave" width="540" height="309" viewBox="0 0 540 309" aria-hidden="true">
      <defs>
        <linearGradient id="crimsonFill" x1="0" y1="0" x2="1" y2="1">
          <stop offset="0" stop-color="#8d1c40"/>
          <stop offset="0.5" stop-color="#b22e57"/>
          <stop offset="1" stop-color="#8a1a3c"/>
        </linearGradient>
      </defs>
      <path d="M0,0 H540 V244 C460,242 400,219 340,199 C270,176 150,129 0,136 Z" fill="var(--wave-grey)"/>
      <path d="M0,0 H540 V230 C460,228 400,205 340,185 C270,162 150,115 0,122 Z" fill="url(#crimsonFill)"/>
    </svg>
    <div class="contact-block">
      <div class="holder-name">THEODORE K. DELCOURT</div>
      <div class="holder-title">President</div>
      <div class="address">41 NE 3RD AVE STE 200<br>MIAMI, FL 33142</div>
      <div class="contact-line">
        <span class="icon">
          <svg width="9" height="9" viewBox="0 0 10 10"><path d="M2 1 L4 1 L4.6 3 L3.4 4 Q4.5 6 6 6.6 L7 5.4 L9 6 L9 8 Q9 9 8 9 Q1 8.5 1 2 Q1 1 2 1Z" fill="#a3264d"/></svg>
        </span>
        +01-305-555-0142
      </div>
      <div class="contact-line">
        <span class="icon">
          <svg width="9" height="9" viewBox="0 0 10 10"><rect x="0.5" y="2" width="9" height="6" fill="none" stroke="#a3264d"/><path d="M0.5 2 L5 5.5 L9.5 2" fill="none" stroke="#a3264d"/></svg>
        </span>
        office@delcourtlawpa.com
      </div>
    </div>
    <div class="firm-lockup">
      <div class="firm-mark" aria-hidden="true"></div>
      <div>
        <div class="firm-name">Delcourt Law, P.A.</div>
        <div class="firm-person">Theodore K. Delcourt</div>
      </div>
    </div>
  </section>

  <section class="card card-firm" aria-label="Business card, firm side">
    <div class="firm-lockup">
      <div class="firm-mark" aria-hidden="true"></div>
      <div>
        <div class="firm-name">Delcourt Law, P.A.</div>
        <div class="firm-person">Theodore K. Delcourt</div>
      </div>
    </div>
  </section>

</body>
</html>
```